Painting Company Business Card

Brightwell Painting needs a new business card. See attachments for our logo and current card as an example.
We want to utilize the same colors in the logo, and keep all the information that is currently on it. Just need an updated and modern design.
We are open to loosing the Association Logos if it means a better design.
We are also entertaining a spot for a picture of a headshot of the person listed on the card. Head shot can be finished later.

```html
<!DOCTYPE html>
<html lang="en">
<head>
<meta charset="utf-8">
<title>Brightwell Painting – Business Card</title>
<link href="https://fonts.googleapis.com/css2?family=Montserrat:wght@300;400;600;700&family=Open+Sans:wght@400;600&display=swap" rel="stylesheet">
<style>
  :root {
    --stage: #e9e8e6;
    --card-dark: #1c1c1c;
    --card-light: #f7f7f5;
    --brand-green: #5b6b45;
    --brand-maroon: #7f3a34;
    --ink: #4a4a4a;
    --ink-soft: #6a6a6a;
    --photo-grey: #7a7a7a;
  }
  * { box-sizing: border-box; margin: 0; padding: 0; }
  html, body { width: 1200px; height: 900px; overflow: hidden; }
  body {
    background: var(--stage);
    position: relative;
    font-family: "Open Sans", Arial, sans-serif;
  }
  .card {
    position: absolute;
    width: 525px;
    height: 300px;
    border-radius: 22px;
    overflow: hidden;
    box-shadow: 0 8px 24px rgba(0,0,0,0.18);
  }

  /* Back of card */
  .card-back {
    left: 70px; top: 130px;
    background: var(--card-dark);
  }
  .card-back .wordmark {
    position: absolute;
    left: 0; right: 0; top: 112px;
    text-align: center;
    font-family: "Montserrat", Arial, sans-serif;
    font-weight: 700;
    font-size: 34px;
    letter-spacing: 0.5px;
    color: var(--brand-green);
  }
  .card-back .services {
    position: absolute;
    left: 0; right: 0; bottom: 34px;
    text-align: center;
    font-size: 12.5px;
    color: #e6e6e6;
    letter-spacing: 0.3px;
  }
  .services .sep { margin: 0 8px; }

  /* Front of card */
  .card-front {
    left: 605px; top: 470px;
    background: var(--card-light);
  }
  .card-front .wordmark {
    position: absolute;
    right: 26px; top: 26px;
    font-family: "Montserrat", Arial, sans-serif;
    font-weight: 700;
    font-size: 19px;
    color: var(--brand-green);
  }
  .headshot-slot {
    position: absolute;
    right: 28px; top: 78px;
    width: 170px; height: 222px;
    border-radius: 70px 70px 0 0;
    background: linear-gradient(180deg, #6e6e6e, var(--photo-grey));
    z-index: 2;
  }
  .band-line {
    position: absolute;
    left: 0; right: 0; bottom: 50px;
    height: 5px;
    background: var(--brand-green);
  }
  .band-fill {
    position: absolute;
    left: 0; right: 0; bottom: 0;
    height: 40px;
    background: var(--brand-maroon);
  }
  .person {
    position: absolute;
    left: 34px; top: 82px;
  }
  .person .name {
    font-family: "Montserrat", Arial, sans-serif;
    font-size: 25px;
    color: var(--brand-maroon);
    letter-spacing: 0.3px;
  }
  .person .name .first { font-weight: 300; }
  .person .name .last { font-weight: 700; }
  .person .role {
    margin-top: 2px;
    font-family: "Montserrat", Arial, sans-serif;
    font-size: 11.5px;
    font-weight: 400;
    color: var(--ink);
    letter-spacing: 0.4px;
  }
  .person .rule {
    margin-top: 6px;
    width: 76px; height: 1.5px;
    background: var(--brand-green);
  }
  .contact {
    position: absolute;
    left: 34px; bottom: 66px;
    list-style: none;
  }
  .contact li {
    display: flex; align-items: center;
    font-size: 13px;
    color: var(--brand-maroon);
    line-height: 20px;
  }
  .contact svg { width: 12px; height: 12px; margin-right: 9px; fill: var(--ink); }
</style>
</head>
<body>

  <section class="card card-back">
    <div class="wordmark">Brightwell Painting</div>
    <p class="services">
      Exterior Painting<span class="sep">|</span>Interior Painting<span class="sep">|</span>Carpentry<span class="sep">|</span>Drywall
    </p>
  </section>

  <section class="card card-front">
    <div class="wordmark">Brightwell Painting</div>

    <div class="person">
      <div class="name"><span class="first">DANIEL</span> <span class="last">HARPER</span></div>
      <div class="role">QUALITY MANAGER</div>
      <div class="rule"></div>
    </div>

    <ul class="contact">
      <li>
        <svg viewBox="0 0 12 12"><path d="M1 4c0-1.5 2-2.5 5-2.5S11 2.5 11 4v1H8.5V4H3.5v1H1z M3 6h6l1.5 4.5h-9z"/></svg>
        555-014-2738
      </li>
      <li>
        <svg viewBox="0 0 12 12"><path d="M0.5 2.5h11v7h-11z M1.2 3.2 6 6.6l4.8-3.4" fill="none" stroke="#4a4a4a" stroke-width="1"/></svg>
        Daniel.Brightwell@mailbox.com
      </li>
      <li>
        <svg viewBox="0 0 12 12"><g fill="none" stroke="#4a4a4a" stroke-width="1"><circle cx="6" cy="6" r="5"/><ellipse cx="6" cy="6" rx="2.2" ry="5"/><path d="M1 6h10"/></g></svg>
        BrightwellPainting.com
      </li>
    </ul>

    <div class="band-line"></div>
    <div class="band-fill"></div>
    <div class="headshot-slot" role="img" aria-label="Headshot photo of the team member, to be added later"></div>
  </section>

</body>
</html>
```